Looking to design a new sign for our church.

Looking for a new sign
4 x 8 feet dimension
We are renaming the church "Medlow Ridge Community Church"
looking for legible graphics
Would like some type of backdrop being a family tree (oak) / open to other ideas as you are led
I have included a pic of the old sign for your review
would like to incorporate our ministry logo on the lower right hand corner of the sign / see file attached

```html
<!DOCTYPE html>
<html lang="en">
<head>
<meta charset="UTF-8">
<title>Medlow Ridge Community Church – Sign</title>
<link href="https://fonts.googleapis.com/css2?family=Bebas+Neue&display=swap" rel="stylesheet">
<style>
  :root {
    --sky-haze: #eef0e4;
    --canopy-light: #8fae4c;
    --canopy-mid: #5d7a2e;
    --canopy-dark: #3a4a22;
    --trunk: #5a4030;
    --meadow: #b9c27a;
    --title-fill: rgba(255, 255, 255, 0.93);
    --title-stroke: #2b2726;
    --panel: rgba(255, 255, 255, 0.62);
    --schedule-blue: #1f5e9c;
    --mark-ink: #1d1d1d;
  }
  * { margin: 0; padding: 0; box-sizing: border-box; }
  html, body { width: 1200px; height: 600px; overflow: hidden; background: #ffffff; }
  .sign {
    position: relative;
    width: 1200px;
    height: 600px;
    overflow: hidden;
    font-family: "Bebas Neue", "Arial Narrow", sans-serif;
  }
  .backdrop {
    position: absolute;
    inset: 0;
    background:
      radial-gradient(ellipse 14% 40% at 54% 85%, var(--trunk) 0%, rgba(90,64,48,0.6) 45%, rgba(90,64,48,0) 100%),
      radial-gradient(ellipse 60% 55% at 50% 30%, var(--canopy-dark) 0%, var(--canopy-mid) 45%, rgba(93,122,46,0) 85%),
      linear-gradient(180deg, var(--canopy-mid) 0%, var(--canopy-light) 40%, var(--sky-haze) 68%, var(--meadow) 78%, var(--canopy-light) 100%);
  }
  .church-title { font-weight: 400; }
  .church-name {
    position: absolute;
    left: 60px;
    width: 1200px;
    text-align: center;
    color: var(--title-fill);
    -webkit-text-stroke: 3px var(--title-stroke);
    paint-order: stroke fill;
    line-height: 1;
    white-space: nowrap;
  }
  .church-name--primary {
    top: 113px;
    font-size: 210px;
    letter-spacing: 2px;
  }
  .church-name--secondary {
    top: 309px;
    font-size: 125px;
    letter-spacing: 1px;
  }
  .schedule-panel {
    position: absolute;
    left: 110px;
    top: 486px;
    width: 1080px;
    height: 114px;
    background: var(--panel);
  }
  .schedule {
    position: absolute;
    left: 75px;
    top: 69px;
    display: flex;
    gap: 16px;
    color: var(--schedule-blue);
    font-size: 31px;
    line-height: 1;
    letter-spacing: 0.5px;
    white-space: nowrap;
  }
  .ministry-name {
    position: absolute;
    left: 1000px;
    top: 34px;
    width: 76px;
    text-align: center;
    color: var(--mark-ink);
    font-size: 16px;
    line-height: 1.05;
  }
  .ministry-name .dot {
    display: block;
    width: 12px;
    height: 12px;
    margin: 0 auto 5px;
    border-radius: 50%;
    background: var(--mark-ink);
  }
</style>
</head>
<body>
  <main class="sign">
    <div class="backdrop" role="img" aria-label="Photograph of a broad old oak tree with spreading branches over a grassy meadow"></div>

    <h1 class="church-title">
      <span class="church-name church-name--primary">Medlow Ridge</span>
      <span class="church-name church-name--secondary">Community Church</span>
    </h1>

    <section class="schedule-panel">
      <p class="schedule">
        <span>10:30AM Worship Service</span>
        <span>|</span>
        <span>9:30AM Sunday School</span>
        <span>|</span>
        <span>6:00PM Wednesday Service</span>
      </p>
      <div class="ministry-name"><span class="dot"></span>Ridgeway<br>Ministries</div>
    </section>
  </main>
</body>
</html>
```